Business Card Design for Colin Metz

I am a DJ who plays electronic music of all kinds - mainly House, Bass Music, U.K. Funky, Trance, Progressive, Breakbeat, Drum & Bass, etc.

```html
<!DOCTYPE html>
<html lang="en">
<head>
<meta charset="utf-8">
<title>Colin Metz – Business Card</title>
<link rel="stylesheet" href="https://fonts.googleapis.com/css2?family=Cinzel:wght@400;600&display=swap">
<style>
  :root {
    --page-bg: #e9e6e1;
    --card-paper: #f3dcb8;
    --card-paper-edge: #e8c99d;
    --name-ember: #b5561c;
    --name-glow: rgba(240, 150, 60, 0.55);
    --contact-ink: #2b1f15;
    --emblem-light: #e6eef5;
    --emblem-sky: #a9c4dc;
    --emblem-ember: #c8692a;
  }
  * { box-sizing: border-box; margin: 0; padding: 0; }
  html, body {
    width: 1200px;
    height: 999px;
    overflow: hidden;
    background: var(--page-bg);
  }
  .business-card {
    position: absolute;
    left: 100px;
    top: 214px;
    width: 1000px;
    height: 571px;
    background: radial-gradient(ellipse at 50% 45%, var(--card-paper) 55%, var(--card-paper-edge) 100%);
    box-shadow: 0 6px 24px rgba(0, 0, 0, 0.18);
    font-family: "Cinzel", "Times New Roman", serif;
    text-align: center;
  }
  .emblem-area {
    position: absolute;
    left: 225px;
    top: 22px;
    width: 550px;
    height: 340px;
  }
  .dj-name {
    position: absolute;
    left: 0;
    right: 0;
    top: 368px;
    font-size: 66px;
    font-weight: 600;
    letter-spacing: 1px;
    color: var(--name-ember);
    text-shadow: 0 0 10px var(--name-glow);
    line-height: 1;
  }
  .contact-list {
    position: absolute;
    left: 0;
    right: 0;
    top: 440px;
    list-style: none;
    font-size: 25px;
    line-height: 38px;
    color: var(--contact-ink);
  }
</style>
</head>
<body>
  <section class="business-card">
    <svg class="emblem-area" viewBox="0 0 550 340" role="img" aria-label="Phoenix emblem with spread wings rising from flames">
      <defs>
        <radialGradient id="emblemFill" cx="50%" cy="45%" r="60%">
          <stop offset="0%" stop-color="var(--emblem-light)"/>
          <stop offset="55%" stop-color="var(--emblem-sky)"/>
          <stop offset="100%" stop-color="var(--emblem-ember)" stop-opacity="0.6"/>
        </radialGradient>
      </defs>
      <ellipse cx="275" cy="165" rx="270" ry="160" fill="url(#emblemFill)" opacity="0.85"/>
    </svg>
    <h1 class="dj-name">Colin Metz</h1>
    <ul class="contact-list">
      <li class="contact-web">Web: www.djcolinmetz.com</li>
      <li class="contact-email">Email: djcolinmetz@mail.com</li>
      <li class="contact-phone">Phone: +852 5550 1234</li>
    </ul>
  </section>
</body>
</html>
```